Postcard Design for Brindlewood Pine Acres LLC

We are a small family owned Christmas tree farm. We work with various groups on their fundraising programs selling wreaths and trees. Our goal is to expand our business, advertising with post cards.

Target Market(s)

Schools, Trail Rangers, various non profit groups

Industry/Entity Type

Advertising

Requirements
Must have
• Front side-

Let us help you develop a successful holiday fundraiser for your group with fresh, fragrant Wisconsin wreaths shipped directly from our farm!

Picture of a real wreath with a red bow and 2 pinecone clusters at 4 o'clock and 8 o'clock.

Contact information -
Brindlewood Pine Acres LLC
www.brindlewoodpineacres.com
555-147-9362

Backside -
We have 2 different type of wreath fundraising programs - mail order and direct distribution. You group can choose to do one or both. Wholesale Christmas trees are also available.

```html
<!DOCTYPE html>
<html lang="en">
<head>
<meta charset="utf-8">
<title>Brindlewood Pine Acres – Fundraiser Postcard</title>
<link rel="stylesheet" href="https://fonts.googleapis.com/css2?family=Montserrat:wght@500;700;800&display=swap">
<style>
  :root {
    --page-bg: #d9dcdc;
    --wood-dark: #4a1a10;
    --wood-mid: #7a2e1c;
    --wood-light: #a4533a;
    --pine-green: #3f5a1e;
    --wreath-green: #2e4a22;
    --paper: #f4f4f2;
    --line-green: #2f7a2a;
    --text-light: #ffffff;
    --photo-light: #c8cbc8;
    --photo-dark: #4c4f4c;
  }
  * { box-sizing: border-box; margin: 0; padding: 0; }
  html, body {
    width: 1200px; height: 1000px; overflow: hidden;
    background: var(--page-bg);
    font-family: "Montserrat", Arial, sans-serif;
  }
  .postcard {
    position: absolute; left: 255px;
    width: 690px; height: 460px;
    overflow: hidden;
    box-shadow: 0 4px 14px rgba(0,0,0,.25);
  }
  .postcard--front { top: 22px; }
  .postcard--back { top: 512px; background: var(--paper); }

  /* Front */
  .door-photo {
    position: absolute; inset: 0;
    background: linear-gradient(100deg, var(--wood-dark), var(--wood-mid) 40%, var(--wood-light) 65%, var(--wood-mid));
  }
  .card-frame {
    position: absolute; inset: 12px;
    border: 4px solid var(--paper);
    pointer-events: none;
  }
  .wreath-photo {
    position: absolute; left: 340px; top: 28px;
    width: 250px; height: 180px;
    background: radial-gradient(ellipse at 50% 50%, var(--wreath-green) 0%, rgba(46,74,34,.85) 45%, rgba(46,74,34,0) 72%);
  }
  .headline-banner {
    position: absolute; left: 0; top: 196px;
    width: 520px; height: 140px;
  }
  .headline-banner svg { position: absolute; inset: 0; }
  .headline-banner__text {
    position: absolute; left: 34px; top: 20px; width: 440px;
    color: var(--text-light); font-weight: 700;
    font-size: 21px; line-height: 25px; letter-spacing: .3px;
  }
  .contact {
    position: absolute; right: 46px; bottom: 46px;
    color: var(--text-light); text-align: left;
  }
  .contact__name { font-weight: 800; font-size: 13px; }
  .contact__web { font-weight: 500; font-size: 12px; margin-top: 2px; }
  .contact__phone { font-weight: 800; font-size: 15px; margin-top: 3px; letter-spacing: .5px; }

  /* Back */
  .farm-photo {
    position: absolute; left: 0; top: 0;
    width: 405px; height: 460px;
    background: linear-gradient(180deg, var(--photo-dark) 0%, #8a8d8a 35%, #2f322f 55%, var(--photo-light) 78%, #e6e8e6 100%);
  }
  .programs-text {
    position: absolute; left: 28px; top: 24px; width: 350px;
    color: var(--text-light); font-weight: 700;
    font-size: 15px; line-height: 20px; text-align: justify;
  }
  .brand-badge {
    position: absolute; left: 30px; bottom: 0;
    width: 150px; height: 100px;
    background: var(--line-green);
    border-radius: 75px 75px 0 0;
    color: var(--text-light); text-align: center;
    padding-top: 30px;
  }
  .brand-badge__name { font-weight: 700; font-size: 15px; line-height: 18px; }
  .brand-badge__web { font-weight: 500; font-size: 7px; margin-top: 8px; }
  .address-lines {
    position: absolute; left: 440px; top: 330px;
    width: 225px;
  }
  .address-lines span {
    display: block; height: 2px; background: var(--line-green);
    margin-bottom: 33px;
  }
</style>
</head>
<body>
  <section class="postcard postcard--front" aria-label="Postcard front">
    <div class="door-photo" role="img" aria-label="Photo of a dark wooden panelled front door"></div>
    <div class="wreath-photo" role="img" aria-label="Photo of a fresh evergreen wreath with a red bow and pinecone clusters"></div>
    <div class="headline-banner">
      <svg width="520" height="140" viewBox="0 0 520 140" aria-hidden="true">
        <polygon points="0,0 520,0 480,70 520,140 0,140" fill="var(--pine-green)"/>
      </svg>
      <p class="headline-banner__text">Let us help you develop a successful holiday fundraiser for your group with fresh, fragrant Wisconsin wreaths shipped directly from our farm!</p>
    </div>
    <div class="contact">
      <p class="contact__name">Brindlewood Pine Acres LLC</p>
      <p class="contact__web">www.brindlewoodpineacres.com</p>
      <p class="contact__phone">555-147-9362</p>
    </div>
    <div class="card-frame"></div>
  </section>

  <section class="postcard postcard--back" aria-label="Postcard back">
    <div class="farm-photo" role="img" aria-label="Black and white photo of rows of Christmas trees on a snowy farm"></div>
    <p class="programs-text">We have 2 different type of wreath fundraising programs – mail order and direct distribution. Your group can choose to do one or both. Wholesale Christmas trees are also available.</p>
    <div class="brand-badge">
      <p class="brand-badge__name">Brindlewood<br>Pine Acres</p>
      <p class="brand-badge__web">www.brindlewoodpineacres.com</p>
    </div>
    <div class="address-lines" aria-hidden="true"><span></span><span></span><span></span></div>
  </section>
</body>
</html>
```